Brush Cutting, Bush Hogging, Forestry Clearing, Dirt Work

We need a business card design design for a new company based in Briarton, LA. We specialize in under-brush clearing, forestry cutting, general bush hogging, heavy duty bush hogging, dirt work, gravel hauling, land clearing . We have bulldozers, compact track loaders, dump trucks, tractors. I will attach a picture of a compact track loader I would like to have on the card design if possible.

Industry/Entity Type

Business

Contact Information for Business Card

Harmon Brush Cutters Briarton, LA. Wade Harmon Doug Swarts601-600-0373 555-017-6480

Font styles to use
Serif
Sans Serif

Requirements
Must have
• Must have a Vantor compact track loader with a brush cutter as the attachment. not a dirt bucket.
Should not have
• should not have any other brand of machine but vantor.

```html
<!DOCTYPE html>
<html lang="en">
<head>
<meta charset="utf-8">
<title>Harmon Brush Cutters – Business Card</title>
<link rel="stylesheet" href="https://fonts.googleapis.com/css2?family=Arimo:ital,wght@0,700;1,400;1,700&display=swap">
<style>
  :root {
    --paper: #fdfdfd;
    --ink: #111111;
    --body-ink: #2a2a2a;
    --accent-yellow: #fbbd16;
    --bar-black: #0c0c0c;
    --machine-light: #d4d4d4;
    --machine-dark: #9a9a9a;
  }
  html, body {
    margin: 0;
    padding: 0;
    overflow: hidden;
    background: var(--paper);
  }
  .card {
    position: relative;
    width: 1200px;
    height: 702px;
    background: var(--paper);
    overflow: hidden;
    font-family: "Arimo", Arial, sans-serif;
  }
  .machine-art {
    position: absolute;
    left: 365px;
    top: 58px;
    width: 810px;
    height: 644px;
  }
  .company-name {
    position: absolute;
    left: 24px;
    top: 18px;
    margin: 0;
    font-size: 63px;
    font-weight: 700;
    letter-spacing: 2px;
    color: var(--ink);
    text-shadow: 2px 2px 1px #8a8a8a;
    white-space: nowrap;
  }
  .company-town {
    position: absolute;
    left: 26px;
    top: 92px;
    margin: 0;
    font-size: 40px;
    font-weight: 700;
    font-style: italic;
    color: var(--ink);
    letter-spacing: 3px;
    white-space: nowrap;
  }
  .bar {
    position: absolute;
    left: 28px;
    width: 44px;
  }
  .bar--contacts { top: 151px; height: 89px; background: var(--bar-black); }
  .bar--services { top: 259px; height: 413px; background: var(--accent-yellow); }
  .contacts {
    position: absolute;
    left: 80px;
    top: 154px;
    margin: 0;
    padding: 0;
    list-style: none;
    font-size: 31px;
    font-style: italic;
    letter-spacing: 2.5px;
    color: var(--body-ink);
    line-height: 39px;
    white-space: nowrap;
  }
  .contacts li { display: flex; }
  .contacts .person { width: 285px; }
  .services {
    position: absolute;
    left: 75px;
    top: 256px;
    font-size: 26px;
    font-style: italic;
    letter-spacing: 1.8px;
    color: var(--body-ink);
    line-height: 33px;
    white-space: nowrap;
  }
  .services p { margin: 0 0 33px 0; }
</style>
</head>
<body>
<div class="card">
  <svg class="machine-art" viewBox="0 0 810 644" role="img" aria-label="Illustration of a compact track loader with front attachment, in grey and pale yellow">
    <defs>
      <linearGradient id="machineTone" x1="0" y1="0" x2="1" y2="1">
        <stop offset="0" stop-color="var(--machine-light)"/>
        <stop offset="0.6" stop-color="#bdbdbd"/>
        <stop offset="1" stop-color="var(--machine-dark)"/>
      </linearGradient>
    </defs>
    <polygon fill="url(#machineTone)" points="300,20 640,0 690,30 700,220 730,360 700,560 520,640 220,644 0,560 80,420 260,350 280,120"/>
  </svg>

  <h1 class="company-name">HARMON BRUSH CUTTERS</h1>
  <p class="company-town">OF BRIARTON, LA</p>

  <div class="bar bar--contacts"></div>
  <ul class="contacts">
    <li><span class="person">WADE HARMON</span><span class="phone">(555)014-2719</span></li>
    <li><span class="person">RICK TOLBEY</span><span class="phone">(555)017-6480</span></li>
  </ul>

  <div class="bar bar--services"></div>
  <div class="services">
    <p>Operating Crews Specialize In:<br>Forestry Cutting, General and Heavy<br>Duty Bush Hogging, Underbrush and<br>Land Clearing, Soil and Gravel<br>Hauled and Worked~</p>
    <p>Our Crews Will Reclaim<br>and Prepare Your<br>Acreage For New<br>Use According To<br>Your Specification<br>In A Timely, Efficient and<br>Saftey Driven Process~</p>
  </div>
</div>
</body>
</html>
```